IT services company needs a business card designed

-2 sided business card.-Front is going to be the logo raised (3D floating effect) on a black background. Make the logos spider web shiny silver and keep the spider the same design. -Back needs to have the following information:Doug Farrow, Managing Partner, Cell: 602-488-3179, Website: Kolvantra.com, Email: Doug@Kolvantra.com
Target Market(s)
IT Services
Industry/Entity Type
It Company
Contact Information for Business Card
-2 sided business card.
-Front is going to be the logo raised (3D floating effect) on a black background. Make the logos spider web shiny silver and keep the spider the same design.
-Back needs to have the following information:
Doug Farrow, Managing Partner, Cell: 602-488-3179, Website: Kolvantra.com, Email: Doug@Kolvantra.com
Look and feel

```html
<!DOCTYPE html>
<html lang="en">
<head>
<meta charset="UTF-8">
<title>Kolvantra Business Card</title>
<link rel="stylesheet" href="https://fonts.googleapis.com/css2?family=Rajdhani:wght@500;600&display=swap">
<style>
  :root {
    --backdrop: #2b2b2d;
    --card-black: #111214;
    --card-white: #f1f2f1;
    --silver: #c9cccf;
    --ink: #1d1e20;
    --accent: #1fa9e6;
    --rule: #8c8f92;
  }
  * { margin: 0; padding: 0; box-sizing: border-box; }
  html, body {
    width: 1200px;
    height: 900px;
    overflow: hidden;
    background: var(--backdrop);
    font-family: "Rajdhani", "Arial Narrow", sans-serif;
  }
  .canvas {
    width: 1200px;
    height: 900px;
    display: flex;
    flex-direction: column;
    align-items: center;
    justify-content: center;
    gap: 44px;
  }
  .card {
    width: 680px;
    height: 388px;
    position: relative;
    box-shadow: 0 6px 18px rgba(0,0,0,0.45);
  }
  .card--front {
    background: var(--card-black);
    display: flex;
    align-items: center;
    justify-content: center;
  }
  .brand {
    display: flex;
    align-items: center;
    gap: 14px;
    font-weight: 600;
    letter-spacing: 0.04em;
    text-transform: uppercase;
  }
  .brand__dot {
    border-radius: 50%;
    flex: none;
  }
  .card--front .brand { font-size: 56px; color: var(--silver); }
  .card--front .brand__dot { width: 18px; height: 18px; background: var(--silver); }

  .card--back {
    background: var(--card-white);
    display: flex;
    align-items: center;
    padding: 0 70px 0 80px;
    gap: 54px;
  }
  .card--back .brand { font-size: 34px; color: var(--ink); }
  .card--back .brand__dot { width: 12px; height: 12px; background: var(--accent); }

  .contact { flex: 1; text-transform: uppercase; }
  .contact__name {
    font-size: 30px;
    font-weight: 600;
    color: var(--accent);
    letter-spacing: 0.03em;
    line-height: 1;
  }
  .contact__title {
    font-size: 18px;
    font-weight: 600;
    color: var(--ink);
    letter-spacing: 0.03em;
    margin-top: 4px;
    padding-bottom: 10px;
    border-bottom: 1.5px solid var(--rule);
  }
  .contact__list { list-style: none; margin-top: 12px; }
  .contact__item {
    display: flex;
    align-items: center;
    gap: 10px;
    font-size: 18px;
    font-weight: 500;
    color: var(--ink);
    line-height: 1.4;
  }
  .contact__icon { width: 15px; height: 15px; flex: none; fill: var(--accent); }
</style>
</head>
<body>
<main class="canvas">
  <section class="card card--front" aria-label="Card front">
    <div class="brand"><span class="brand__dot"></span>Kolvantra</div>
  </section>

  <section class="card card--back" aria-label="Card back">
    <div class="brand"><span class="brand__dot"></span>Kolvantra</div>
    <div class="contact">
      <h1 class="contact__name">Doug Farrow</h1>
      <p class="contact__title">Managing Partner</p>
      <ul class="contact__list">
        <li class="contact__item">
          <svg class="contact__icon" viewBox="0 0 16 16" aria-hidden="true"><path d="M4 0h8a1.5 1.5 0 0 1 1.5 1.5v13A1.5 1.5 0 0 1 12 16H4a1.5 1.5 0 0 1-1.5-1.5v-13A1.5 1.5 0 0 1 4 0zm0.5 2v10h7V2zm3.5 11a1 1 0 1 0 0 2 1 1 0 0 0 0-2z"/></svg>
          602-488-3179
        </li>
        <li class="contact__item">
          <svg class="contact__icon" viewBox="0 0 16 16" aria-hidden="true"><path d="M0 3h16v1.2L8 9 0 4.2zm0 2.6l8 4.8 8-4.8V13H0z"/></svg>
          Doug@Kolvantra.com
        </li>
        <li class="contact__item">
          <svg class="contact__icon" viewBox="0 0 16 16" aria-hidden="true"><circle cx="8" cy="8" r="8"/><path d="M1 8h14M8 1c-2.5 3-2.5 11 0 14M8 1c2.5 3 2.5 11 0 14" stroke="#f1f2f1" stroke-width="1" fill="none"/></svg>
          Kolvantra.com
        </li>
      </ul>
    </div>
  </section>
</main>
</body>
</html>
```